Business card and stationery
Clear Harbour
Project: Business card and stationery
Business card and stationery  -
Creative Brief
Simple
Name Surname
Executive Director
317 Larkmoor Lane, #03 Fenwick Plaza, Country 264519
vantolemu@mailpost.example
www.clearharbour.example.sg
info (name, address, email etc) on the card should be editable for each employee

```html
<!DOCTYPE html>
<html lang="en">
<head>
<meta charset="utf-8">
<title>Clear Harbour — Business Card</title>
<link rel="stylesheet" href="https://fonts.googleapis.com/css2?family=Open+Sans:wght@400;600;700&display=swap">
<style>
  :root {
    --stage: #ecebe8;
    --card: #ffffff;
    --blue: #2f6fe8;
    --green: #3fb82c;
    --ink-blue: #2a6be0;
    --ink: #3a3a3a;
  }
  * { box-sizing: border-box; margin: 0; padding: 0; }
  html, body { width: 1200px; height: 581px; overflow: hidden; }
  body {
    background: var(--stage);
    font-family: "Open Sans", Arial, sans-serif;
    position: relative;
  }
  .card {
    position: absolute;
    top: 144px;
    width: 466px;
    height: 293px;
    background: var(--card);
    border-radius: 16px;
    overflow: hidden;
    box-shadow: 0 6px 16px rgba(0,0,0,0.18);
  }
  .card--front { left: 125px; }
  .card--back { left: 605px; }

  .front-shape { position: absolute; inset: 0; width: 100%; height: 100%; }

  .brand {
    position: absolute;
    display: flex;
    flex-direction: column;
    align-items: center;
    gap: 10px;
  }
  .brand__dot {
    width: 44px; height: 44px;
    border-radius: 50%;
    background: var(--green);
  }
  .brand__name {
    font-weight: 700;
    color: var(--ink-blue);
    font-size: 30px;
    letter-spacing: -0.5px;
    white-space: nowrap;
  }
  .card--front .brand { left: 8px; top: 72px; width: 180px; }
  .card--front .brand__dot { width: 40px; height: 40px; }
  .card--front .brand__name { font-size: 23px; letter-spacing: -0.6px; }
  .card--back .brand { left: 0; right: 0; top: 90px; }

  .details {
    position: absolute;
    right: 18px;
    top: 20px;
    width: 200px;
    text-align: right;
    color: #fff;
  }
  .details__name { font-size: 19px; font-weight: 700; line-height: 1.2; }
  .details__role { font-size: 11px; font-weight: 600; margin-top: 2px; }
  .details__address { font-size: 11.5px; line-height: 1.45; margin-top: 58px; }
  .details__contacts { list-style: none; margin-top: 14px; font-size: 11px; line-height: 1.75; }
  .details__contacts li { display: flex; justify-content: flex-end; align-items: center; gap: 7px; white-space: nowrap; }
  .details__contacts svg { width: 11px; height: 11px; flex: none; }

  .web {
    position: absolute;
    left: 0; right: 0; bottom: 26px;
    text-align: center;
    font-size: 14px;
    font-weight: 600;
    color: var(--ink);
  }
</style>
</head>
<body>
  <section class="card card--front">
    <svg class="front-shape" viewBox="0 0 466 293" preserveAspectRatio="none" aria-hidden="true">
      <path d="M222 0 C188 70 188 220 232 293 L246 293 C204 220 204 70 238 0 Z" fill="var(--green)"/>
      <path d="M240 0 C206 70 206 220 248 293 L466 293 L466 0 Z" fill="var(--blue)"/>
    </svg>

    <div class="brand">
      <span class="brand__dot"></span>
      <span class="brand__name">Clear Harbour</span>
    </div>

    <div class="details">
      <p class="details__name">Name Surname</p>
      <p class="details__role">Executive Director</p>
      <p class="details__address">317 Larkmoor Lane,<br>#03 Fenwick Plaza,<br>Country 264519</p>
      <ul class="details__contacts">
        <li>+65 6120 4581
          <svg viewBox="0 0 12 12"><path d="M3 1 L5 3.5 L4 5 C5 7 6 8 7.5 8.5 L9 7.5 L11 9.5 L9.5 11 C5 11 1 7 1 2.5 Z" fill="#fff"/></svg></li>
        <li>+65 9134 7702
          <svg viewBox="0 0 12 12"><rect x="3" y="0.5" width="6" height="11" rx="1.2" fill="#fff"/><rect x="4" y="2" width="4" height="7" fill="var(--blue)"/></svg></li>
        <li>vantolemu@mailpost.example
          <svg viewBox="0 0 12 12"><circle cx="6" cy="6" r="5.5" fill="#fff"/><rect x="3" y="4" width="6" height="4.2" fill="none" stroke="var(--blue)"/><path d="M3 4 L6 6.5 L9 4" fill="none" stroke="var(--blue)"/></svg></li>
        <li>www.clearharbour.example.sg
          <svg viewBox="0 0 12 12"><circle cx="6" cy="6" r="5.2" fill="none" stroke="#fff" stroke-width="1.2"/><ellipse cx="6" cy="6" rx="2.2" ry="5.2" fill="none" stroke="#fff"/><line x1="1" y1="6" x2="11" y2="6" stroke="#fff"/></svg></li>
      </ul>
    </div>
  </section>

  <section class="card card--back">
    <div class="brand">
      <span class="brand__dot"></span>
      <span class="brand__name">Clear Harbour</span>
    </div>
    <p class="web">www.clearharbour.example.sg</p>
  </section>
</body>
</html>
```